New funky, super creative logo design for printing business

Stamp, Wrap and Ship

We are a new digital printing business, based on the Gold Coast of Australia. We have a web site under construction - www.stampwrapandship.net, which will aim at the Business to Business market. We are digital printers, offering a wide variety of print products from business cards to wide format print jobs for consumers and small to medium sized business'. We offer up to date technological, digital and wide format print, at hi octane speed. Our prices are very competitive, and turnaround is super fast.

We like to think outside the box, and this should shine through in the design and colours that you use. Be bold and creative, we want to stand out from the crowd.

We will also soon be needing a full suite of marketing collaterals - posters, letterheads, scrap pads, calendars, banners etc. but this will come later, once we have decided on the logo and layouts.

We want a vibrant, bold image, communicating vibrancy and excitement.

Details on the card are company name: Stamp, Wrap and Ship.
www.stampwrapandship.net.
contact: Corinne (+61)437182265
e-mail:corinne@stampwrapandship.net

I must be able to change some of the details such as the name and number on the card.

Target Market(s)

Business to business, small retail, some individuals

Industry/Entity Type

Construction

Requirements
Must have
• Unique funky logo.
Nice to have
• A three dimensional look,with depth in the logo.

```html
<!DOCTYPE html>
<html lang="en">
<head>
<meta charset="utf-8">
<title>Stamp, Wrap and Ship – Business Card</title>
<link rel="stylesheet" href="https://fonts.googleapis.com/css2?family=Share+Tech+Mono&display=swap">
<style>
  :root {
    --teal: #7dc6bd;
    --sun: #fdd27e;
    --cream: #f6efc3;
    --paper: #ffffff;
  }
  * { margin: 0; padding: 0; box-sizing: border-box; }
  html, body {
    width: 937px;
    height: 1200px;
    overflow: hidden;
    background: var(--paper);
  }
  .canvas {
    position: relative;
    width: 937px;
    height: 1200px;
    font-family: "Share Tech Mono", monospace;
  }
  .card {
    position: absolute;
    background: var(--teal);
    overflow: hidden;
  }
  .card--front { left: 0; top: 0; width: 935px; height: 600px; }
  .card--back { left: 1px; top: 602px; width: 932px; height: 596px; }

  .dot-row { position: absolute; left: 0; width: 935px; height: 20px; }
  .dot-row--top { top: 26px; }
  .dot-row--bottom { top: 558px; }

  .disc {
    position: absolute;
    border-radius: 50%;
    background: var(--sun);
  }
  .card--front .disc { left: 224px; top: 55px; width: 492px; height: 492px; }
  .card--back .disc { left: 214px; top: 13px; width: 490px; height: 490px; }

  /* Brand name: one font, one weight, one colour */
  .wordmark {
    position: absolute;
    left: 224px; top: 55px; width: 492px; height: 492px;
    color: var(--cream);
    text-align: center;
    font-weight: 400;
  }
  .wordmark span {
    position: absolute;
    left: 0; right: 0;
    line-height: 1;
  }
  .wordmark .w1 { top: 86px; font-size: 66px; letter-spacing: -1px; }
  .wordmark .w2 { top: 160px; font-size: 84px; letter-spacing: 2px; }
  .wordmark .w3 { top: 284px; font-size: 40px; }
  .wordmark .w4 { top: 350px; font-size: 64px; letter-spacing: 1px; }

  .contact {
    position: absolute;
    left: 214px; width: 490px;
    color: var(--cream);
    text-align: center;
    white-space: nowrap;
  }
  .contact__title {
    top: 98px;
    font-size: 31px;
    font-style: italic;
    letter-spacing: 9px;
    line-height: 46px;
  }
  .contact__details {
    top: 234px;
    font-size: 27px;
    letter-spacing: 7px;
    line-height: 42px;
    font-variant: small-caps;
  }
  .website {
    position: absolute;
    left: 0; width: 932px;
    top: 525px;
    text-align: center;
    color: var(--sun);
    font-size: 31px;
    letter-spacing: 7px;
  }
</style>
</head>
<body>
<main class="canvas">

  <section class="card card--front" aria-label="Card front">
    <svg class="dot-row dot-row--top" viewBox="0 0 935 20" aria-hidden="true">
      <g fill="#fdd27e">
        <circle cx="231" cy="10" r="8"/><circle cx="279" cy="10" r="8"/><circle cx="327" cy="10" r="8"/>
        <circle cx="374" cy="10" r="8"/><circle cx="422" cy="10" r="8"/><circle cx="470" cy="10" r="8"/>
        <circle cx="517" cy="10" r="8"/><circle cx="565" cy="10" r="8"/><circle cx="613" cy="10" r="8"/>
        <circle cx="660" cy="10" r="8"/><circle cx="708" cy="10" r="8"/>
      </g>
    </svg>
    <div class="disc"></div>
    <h1 class="wordmark" aria-label="Stamp, Wrap and Ship">
      <span class="w1">STAMP,</span>
      <span class="w2">WRAP</span>
      <span class="w3">&amp;</span>
      <span class="w4">SHIP</span>
    </h1>
    <svg class="dot-row dot-row--bottom" viewBox="0 0 935 20" aria-hidden="true">
      <g fill="#fdd27e">
        <circle cx="231" cy="10" r="8"/><circle cx="279" cy="10" r="8"/><circle cx="327" cy="10" r="8"/>
        <circle cx="374" cy="10" r="8"/><circle cx="422" cy="10" r="8"/><circle cx="470" cy="10" r="8"/>
        <circle cx="517" cy="10" r="8"/><circle cx="565" cy="10" r="8"/><circle cx="613" cy="10" r="8"/>
        <circle cx="660" cy="10" r="8"/><circle cx="708" cy="10" r="8"/>
      </g>
    </svg>
  </section>

  <section class="card card--back" aria-label="Card back">
    <div class="disc"></div>
    <p class="contact contact__title">STAMP, WRAP &amp;<br>SHIP.</p>
    <p class="contact contact__details">
      - Corinne -<br>
      p. +61437182265<br>
      e. corinne@stamp-<br>
      wrapandship.net
    </p>
    <p class="website">WWW.STAMPWRAPANDSHIP.NET</p>
  </section>

</main>
</body>
</html>
```